The Pixel Tavern Business card.

A Simple card with our Logo and contact information. To give to investors and other professionals.

We are a nerd themed bar.
our target market is young professionals age 21+ but the real purpose of this business card is to present to potential investors and other professionals with our contact information. as we are still looking for funding before we start up.

I am partial to green and my partner likes red we are open to iteration.

Target Market(s)

Investors

Industry/Entity Type

Business

Contact Information for Business Card

Marcus Henley (555) 730-6621 kent.w4100@mailbox-demo.net Brian Tolle (555) 918-2047 briant731@mailbox-demo.net

Font styles to use
Serif

Requirements
Nice to have
• Keep it simple but not boring.
• Use the Logos but feel free to edit them to match theme/colors.
• Keep the back clean and use one of the Logos.

```html
<!DOCTYPE html>
<html lang="en">
<head>
<meta charset="utf-8">
<title>The Pixel Tavern – Business Card</title>
<link rel="stylesheet" href="https://fonts.googleapis.com/css2?family=Merriweather:wght@400;700&display=swap">
<style>
  :root {
    --backdrop-top: #b9c2cf;
    --backdrop-bottom: #e9edf2;
    --wine-light: #5e1a1b;
    --wine-dark: #2e0a0b;
    --olive: #6f8a34;
    --olive-dark: #5a7229;
    --gold: #d8b56e;
    --gold-soft: #c9a35e;
    --gap-red: #5a1416;
  }
  * { margin: 0; padding: 0; box-sizing: border-box; }
  html, body {
    width: 1200px;
    height: 675px;
    overflow: hidden;
  }
  body {
    background: linear-gradient(180deg, var(--backdrop-top), var(--backdrop-bottom));
    font-family: "Merriweather", Georgia, serif;
  }
  .business-card {
    position: absolute;
    left: 75px;
    top: 37px;
    width: 1050px;
    height: 600px;
    overflow: hidden;
    background: radial-gradient(ellipse at 55% 40%, var(--wine-light), var(--wine-dark) 85%);
    box-shadow: 0 18px 40px rgba(40, 50, 70, 0.35);
  }
  .card-art {
    position: absolute;
    inset: 0;
    width: 100%;
    height: 100%;
  }
  .brand {
    position: absolute;
    left: 130px;
    top: 350px;
    display: flex;
    align-items: center;
    gap: 16px;
  }
  .brand-dot {
    width: 26px;
    height: 26px;
    border-radius: 50%;
    background: var(--gold);
  }
  .brand-name {
    font-weight: 700;
    font-size: 46px;
    color: var(--gold);
    letter-spacing: 1px;
  }
  .contact {
    position: absolute;
    color: var(--gold-soft);
    line-height: 1.4;
  }
  .contact-name {
    font-weight: 700;
    color: var(--gold);
  }
  .contact--primary {
    left: 245px;
    top: 440px;
    font-size: 23px;
  }
  .contact--primary .contact-name { font-size: 32px; }
  .contact--secondary {
    left: 680px;
    top: 250px;
    font-size: 17px;
  }
  .contact--secondary .contact-name { font-size: 25px; }
</style>
</head>
<body>
  <div class="business-card">
    <svg class="card-art" viewBox="0 0 1050 600" preserveAspectRatio="none">
      <path class="gold-band" d="M0,0 H1010 C815,125 410,282 0,346 Z" fill="#d8b56e"/>
      <path class="red-gap" d="M0,0 H978 C792,107 400,262 0,322 Z" fill="#5a1416"/>
      <g role="img" aria-label="Olive green panel with a repeating gold ornamental damask pattern">
        <path class="pattern-panel" d="M0,0 H948 C765,92 382,244 0,306 Z" fill="#6f8a34"/>
      </g>
    </svg>

    <div class="brand">
      <span class="brand-dot"></span>
      <span class="brand-name">The Pixel Tavern</span>
    </div>

    <div class="contact contact--primary">
      <p class="contact-name">Marcus Henley</p>
      <p>Phone: (555) 730-6621</p>
      <p>Email: kent.w4100@mailbox-demo.net</p>
    </div>

    <div class="contact contact--secondary">
      <p class="contact-name">Brian Tolle</p>
      <p>Phone: (555) 918-2047</p>
      <p>Email: briant731@mailbox-demo.net</p>
    </div>
  </div>
</body>
</html>
```